Customer Upgrade from Free to Paid Investment Management

Our intent is to have customers that use our free online service consider converting into our paid investment management service.

In current vernacular, we have a Freemium business proposition - but we are just at the early stages of building out our upgrade capabilities.

The design request is detailed in the attached file, but essentially, I'm looking to add another banner to our library. Let me see what you can do!

Target Market(s)

40s-50s, can have any balance in their 401k, at first thought they could manage their 401k themselves, but may be interested in having us manage.

Industry/Entity Type

Investment

Requirements
Must have
• Keep it very simple.
Banner specs are attached in the file
Should not have
• No animation
No "hard sell"

```html
<!DOCTYPE html>
<html lang="en">
<head>
<meta charset="utf-8">
<title>Upgrade Banners</title>
<link rel="stylesheet" href="https://fonts.googleapis.com/css2?family=Arimo:wght@400;700&display=swap">
<style>
  :root {
    --bg-dark: #141414;
    --bg-glow: #4a4a4a;
    --banner-top: #ffffff;
    --banner-bottom: #cfe8f7;
    --headline: #e8731b;
    --body-text: #111111;
    --button-top: #f9a53c;
    --button-bottom: #ea7410;
    --button-edge: #d4650c;
    --icon-blue: #1b73c8;
    --icon-blue-light: #5fb4f0;
    --icon-rim: #e6e9ee;
    --placeholder-a: #dfe6ee;
    --placeholder-b: #9fb5cc;
  }
  * { margin: 0; padding: 0; box-sizing: border-box; }
  html, body { width: 1200px; height: 524px; overflow: hidden; }
  body {
    background: radial-gradient(ellipse 55% 75% at 50% 48%, var(--bg-glow) 0%, #2c2c2c 55%, var(--bg-dark) 100%);
    font-family: "Arimo", Arial, sans-serif;
    position: relative;
  }
  .banner {
    position: absolute;
    left: 148px;
    width: 886px;
    height: 103px;
    background: linear-gradient(to bottom, var(--banner-top) 0%, var(--banner-bottom) 100%);
  }
  .banner--help { top: 123px; }
  .banner--managed { top: 290px; }
  .banner__copy {
    position: absolute;
    left: 150px;
    width: 490px;
    top: 18px;
    text-align: center;
  }
  .banner__headline {
    color: var(--headline);
    font-weight: 700;
    font-size: 23px;
    line-height: 30px;
  }
  .banner__line {
    color: var(--body-text);
    font-size: 23px;
    line-height: 32px;
  }
  .cta {
    position: absolute;
    left: 644px;
    top: 31px;
    width: 188px;
    height: 43px;
    border-radius: 5px;
    background: linear-gradient(to bottom, var(--button-top), var(--button-bottom));
    border: 1px solid var(--button-edge);
    box-shadow: 0 2px 3px rgba(0,0,0,0.25);
    color: #fff;
    font-size: 21px;
    display: flex;
    align-items: center;
    padding-left: 17px;
    gap: 8px;
    text-decoration: none;
  }
  .cta__arrow { width: 26px; height: 26px; }
  .icon-help {
    position: absolute;
    left: 164px;
    top: 109px;
    width: 124px;
    height: 124px;
  }
  .icon-managed {
    position: absolute;
    left: 157px;
    top: 265px;
    width: 124px;
    height: 121px;
    border-radius: 6px;
    background: linear-gradient(135deg, var(--placeholder-a), var(--placeholder-b));
  }
</style>
</head>
<body>
  <section class="banner banner--help">
    <div class="banner__copy">
      <p class="banner__headline">Not sure what to do from here?</p>
      <p class="banner__line">It’s ok if you don’t know what to do next</p>
    </div>
    <a class="cta" href="#">Learn More!
      <svg class="cta__arrow" viewBox="0 0 26 26"><circle cx="13" cy="13" r="12" fill="#f7f1e6"/><path d="M7 11h7V7l6 6-6 6v-4H7z" fill="#ea7410"/></svg>
    </a>
  </section>

  <svg class="icon-help" viewBox="0 0 124 124" aria-label="Help icon">
    <defs>
      <radialGradient id="help-fill" cx="45%" cy="35%" r="70%">
        <stop offset="0" stop-color="var(--icon-blue-light)"/>
        <stop offset="1" stop-color="var(--icon-blue)"/>
      </radialGradient>
    </defs>
    <circle cx="62" cy="62" r="60" fill="var(--icon-rim)" stroke="#b8bec7" stroke-width="2"/>
    <circle cx="62" cy="60" r="48" fill="url(#help-fill)"/>
    <text x="62" y="82" text-anchor="middle" font-family="Arimo, Arial, sans-serif" font-weight="700" font-size="62" fill="#fff">?</text>
  </svg>

  <section class="banner banner--managed">
    <div class="banner__copy">
      <p class="banner__headline">Want us to manage this for you?</p>
      <p class="banner__line">You are in charge, we can do the work</p>
    </div>
    <a class="cta" href="#">Learn More!
      <svg class="cta__arrow" viewBox="0 0 26 26"><circle cx="13" cy="13" r="12" fill="#f7f1e6"/><path d="M7 11h7V7l6 6-6 6v-4H7z" fill="#ea7410"/></svg>
    </a>
  </section>

  <div class="icon-managed" role="img" aria-label="Computer monitor with a settings gear illustration"></div>
</body>
</html>
```